Modern & Aesthetic Electrician Sign Design for Work Vehicle

Modern and aesthetic signage design for an electricians work vehicle. Including already designed logo, mobile number, ABN, licensing number and services offered. Preference is black background, symmetric design with logo centred, services offered at bottom of sign in smaller size font. Mobile number readable and big enough to standout without being too large.

Industry/Entity Type

Electrician

Font styles to use
Serif
Sans Serif

Colors
000000
ffffff
ec1f27

Requirements
Must have
• Logo
• Services Offered
• Mobile Number
• ABN
• License Number
• Black background

```html
<!DOCTYPE html>
<html lang="en">
<head>
<meta charset="utf-8">
<title>Ridgeway Electrical – Vehicle Signage</title>
<link rel="stylesheet" href="https://fonts.googleapis.com/css2?family=Roboto+Condensed:wght@400;700&display=swap">
<style>
  :root {
    --black: #000000;
    --white: #ffffff;
    --red: #ec1f27;
    --grey: #8e8e8e;
    --label: #222222;
    --page: #ffffff;
  }
  * { margin: 0; padding: 0; box-sizing: border-box; }
  html, body {
    width: 1200px; height: 800px; overflow: hidden;
    background: var(--page);
    font-family: "Roboto Condensed", "Arial Narrow", sans-serif;
  }
  .canvas { position: relative; width: 1200px; height: 800px; }

  .sheet-label {
    position: absolute;
    font-size: 18px;
    color: var(--label);
    font-weight: 400;
  }

  /* Back panel */
  .back-panel {
    position: absolute; left: 12px; top: 30px;
    width: 775px; height: 305px;
    background: var(--black);
  }
  .back-panel .call {
    position: absolute; left: 44px; top: 52px;
    font-size: 56px; font-weight: 400; color: var(--red); line-height: 1;
  }
  .back-panel .phone {
    position: absolute; left: 42px; top: 118px;
    font-size: 82px; font-weight: 400; color: var(--white); line-height: 1;
    letter-spacing: 1px;
  }
  .back-brand {
    position: absolute; left: 516px; top: 50px; width: 240px;
    display: flex; flex-direction: column; align-items: center;
  }
  .back-brand .mark {
    width: 148px; height: 148px; border-radius: 50%;
    border: 7px solid var(--grey);
  }
  .back-brand .name {
    margin-top: 22px;
    font-size: 40px; font-weight: 700; color: var(--red);
    line-height: 1; text-align: center; letter-spacing: 1px;
  }

  /* Side panel */
  .side-panel {
    position: absolute; left: 390px; top: 470px;
    width: 800px; height: 230px;
    background: var(--black);
    border-radius: 18px;
  }
  .abn { position: absolute; left: 107px; top: 75px; line-height: 1.1; }
  .abn .key { font-size: 10px; color: var(--red); }
  .abn .value { font-size: 12px; color: var(--white); }

  .side-brand {
    position: absolute; left: 230px; top: 64px; width: 140px;
    display: flex; flex-direction: column; align-items: center;
  }
  .side-brand .mark {
    width: 54px; height: 54px; border-radius: 50%;
    border: 3px solid var(--grey);
  }
  .side-brand .name {
    margin-top: 8px;
    font-size: 16px; font-weight: 700; color: var(--red);
    line-height: 1; text-align: center;
  }
  .side-brand .services {
    margin-top: 6px;
    font-size: 13px; color: var(--white);
  }

  .side-contact { position: absolute; left: 602px; top: 48px; }
  .side-contact .call { font-size: 21px; color: var(--red); line-height: 1; }
  .side-contact .phone { font-size: 27px; color: var(--white); line-height: 1.05; }
  .licence { margin-left: 78px; margin-top: 2px; line-height: 1.1; }
  .licence .key { font-size: 9px; color: var(--red); }
  .licence .value { font-size: 11px; color: var(--white); }
</style>
</head>
<body>
<main class="canvas">

  <section class="back-panel" aria-label="Rear tailgate sign">
    <p class="call">Call Us!</p>
    <p class="phone">000 000 0000</p>
    <div class="back-brand">
      <div class="mark" aria-hidden="true"></div>
      <p class="name">RIDGEWAY ELECTRICAL</p>
    </div>
  </section>
  <p class="sheet-label" style="left:12px; top:342px;">Back design</p>

  <section class="side-panel" aria-label="Vehicle side sign">
    <div class="abn">
      <p class="key">ABN</p>
      <p class="value">00 000 000 000</p>
    </div>
    <div class="side-brand">
      <div class="mark" aria-hidden="true"></div>
      <p class="name">RIDGEWAY ELECTRICAL</p>
      <p class="services">Services Offered</p>
    </div>
    <div class="side-contact">
      <p class="call">Call Us!</p>
      <p class="phone">000 000 0000</p>
      <div class="licence">
        <p class="key">License Number</p>
        <p class="value">00 000 000 000</p>
      </div>
    </div>
  </section>
  <p class="sheet-label" style="left:319px; top:740px;">Side design</p>

</main>
</body>
</html>
```